Wendrik - 3 Etiketten für naturbelassenes Speiseöl - Leinöl, Leindotteröl und Rapsöl
Zielgruppe
Wir sind ein junges Startup mit der Ziel, die besten, gesündesten Omega3-Öle in bester handwerklicher Qualität anzubieten. Vor allem soll das folgende Unterscheidungsmerkmal unsere Marke verkörpern: in Supermärkten und Discountern gibt es überwiegend denaturierte Öle, das heißt extrahierte und raffinierte Öle. Dadurch sind diese zwar länger haltbar, jedoch wertlos für den Körper. Wir wollen Öle voller Naturkraft anbieten und lassen daher die bei Ölpressung entstehenden Schwebestoffe im Form gesunder sekundärer Pflanzenstoffe bewusst im Öl und filtern diese nicht heraus.
Unser Markenname - Wendrik … mit dem Slogan ' Wendrik sein heißt für uns: dynamisch, kraftvoll, vital, frohen Mutes und voller Lebendigkeit - genauso ist unser Öl. Frisch gepresst in bester handwerklicher Qualität, naturbelassen voller gesunder sekundärer Pflanzenstoffe und reich an lebenswichtigen Omega3-Fettsäuren.'
Fokus der Wendrik-Ölmanufakur: echtes Handwerk, beste Qualität, pure Leidenschaft, wahre Nachhaltigkeit und authentische Regionalität!
Aufgabenstellung
In Summe benötigen wir 3 Etiketten für 3 verschiedene Speiseöle: Leinöl, Leindotteröl und Rapsöl.
Für diese drei Öle benötigen wir das Design kreativer, ansprechender Etiketten mit folgenden Prämissen:
A. Etiketten im Tafelkreidestil (Chalk-Handlettering): gemäß unser Vision wollen wir die besten, gesündesten Omega3-Öle in bester handwerklicher Qualität anbieten - diesen Aspekt soll das Look&Feel der Ölflasche samt Etikett verkörpern. Abgefüllt wird unser Öl in hochwertige mattschwarze Steinzeugölflaschen mit Holzkorkverschluss (siehe beigefügtes Bild). Durch das matte schwarz der Ölfalsche soll grundsätzlich das Etiketten-Design im Tafelkreidestil (Chalk-Handlettering) mit einem kreativen Mix aus schönen (gut lesbaren) Schriften und graphischen Elementen sein. Das Endprodukt des Etiketts soll ein transparenter Aufkleber sein, der auf die Flasche geklebt wird.
Maximale Größe des Etiketts: 200ml Flasche max. 13,5 cm Höhe x max. 17 cm Breite
Hinweis: das Etikett soll für die Größe der 200ml Flasche konzipiert werden, jedoch idealerweise so skalierbar sein, daß es auch auf die Größe einer 500 ml-Flasche angepasst werden kann; Größe der 500 ml Flasche max. Höhe 17 cm x max. Breite 21,5 cm
B. Pflanzen-/Saatenzweig als graphisches Unterscheidungsmerkmal des Öls: idealerweise wird das jeweilige Öl (Rapsöl, Leinöl und Leindotteröl) mit einem graphischen Pflanzenzweig der jeweiligen Ölsaat gekennzeichnet.
C. Was macht dies Öl so wertvoll? - die wichtigen und wertvollsten Inhaltsstoffe des jeweiligen Öls sollen herausgestellt werden.
Bein Leinöl und Leindotteröl ist dies vor allem der hohe Gehalt an Omega3-Fettsäuren - dies macht das Öl so besonders wertvoll
Graphisches Textelement mit 'Der Omega3 Booster fur den Körper' (oder der “Powerlieferant” für Omega 3)
Gut für: Herz-Kreislaufszsystem stärken
Gehirnleistung steigern
Blu..

```html
<!DOCTYPE html>
<html lang="de">
<head>
<meta charset="utf-8">
<title>Wendrik – Öletiketten</title>
<link href="https://fonts.googleapis.com/css2?family=Rubik+Dirt&family=Oswald:wght@300;400&family=Montserrat:wght@400&display=swap" rel="stylesheet">
<style>
  :root {
    --page: #ffffff;
    --label: #15141a;
    --chalk: #f4f2ec;
    --chalk-soft: #e6e4de;
    --dotter: #f2e08a;
    --flax-blue: #4a57d6;
    --rape-yellow: #e8c94a;
    --omega-green: #6a9a2a;
  }
  * { margin: 0; padding: 0; box-sizing: border-box; }
  html, body { width: 1200px; height: 1039px; overflow: hidden; background: var(--page); }
  .canvas { position: relative; width: 1200px; height: 1039px; }

  .label {
    position: absolute; top: 150px; width: 290px; height: 845px;
    background: var(--label); border-radius: 60px 60px 14px 14px;
    color: var(--chalk);
  }
  .label--lein { left: 114px; }
  .label--dotter { left: 463px; }
  .label--raps { left: 803px; }

  .brand { position: absolute; top: 134px; left: 0; width: 100%; text-align: center; }
  .brand__row { display: inline-flex; align-items: center; gap: 6px; }
  .brand__dot { width: 14px; height: 14px; border-radius: 50%; background: var(--chalk); }
  .brand__name { font-family: "Montserrat", sans-serif; font-size: 22px; color: var(--chalk); }

  .plant { position: absolute; }

  .title {
    position: absolute;
    writing-mode: vertical-rl; transform: rotate(180deg);
    font-family: "Rubik Dirt", sans-serif; font-size: 60px; line-height: 56px;
    letter-spacing: 8px; color: var(--chalk); white-space: nowrap;
  }
  .title__accent { color: var(--dotter); }

  .badge { position: absolute; width: 80px; height: 80px; border-radius: 50%; background: var(--omega-green); opacity: .92; }

  .benefits { position: absolute; list-style: none; font-family: "Oswald", sans-serif; font-weight: 300; font-size: 14.5px; line-height: 18px; color: var(--chalk); }
  .benefits li { margin-bottom: 12px; }
  .volume { position: absolute; font-family: "Oswald", sans-serif; font-weight: 400; font-size: 26px; color: var(--chalk); }
</style>
</head>
<body>
<main class="canvas">

  <section class="label label--lein">
    <div class="brand">
      <div class="brand__row"><span class="brand__dot"></span><span class="brand__name">Wendrik</span></div>
    </div>
    <svg class="plant" style="left:0;top:320px" width="130" height="480" role="img" aria-label="Gezeichneter Leinblütenzweig vor blauem Aquarellfleck">
      <defs><radialGradient id="blueWash"><stop offset="0" stop-color="#3f4fe0"/><stop offset="1" stop-color="#5a66d8" stop-opacity=".85"/></radialGradient></defs>
      <circle cx="74" cy="110" r="72" fill="url(#blueWash)"/>
      <line x1="74" y1="40" x2="74" y2="473" stroke="var(--chalk-soft)" stroke-width="3" opacity=".7"/>
    </svg>
    <h2 class="title" style="left:124px;bottom:350px">LEINÖL</h2>
    <div class="badge" style="left:171px;top:270px" role="img" aria-label="Omega-3 Siegel"></div>
    <ul class="benefits" style="left:132px;top:521px">
      <li>dynamisch</li><li>vital</li><li>kraftvoll</li><li>frisch<br>gepresst</li><li>naturbelassen</li><li>reich an<br>Omega3<br>Fettsäuren</li>
    </ul>
    <div class="volume" style="left:132px;top:763px">200ml</div>
  </section>

  <section class="label label--dotter">
    <div class="brand">
      <div class="brand__row"><span class="brand__dot"></span><span class="brand__name">Wendrik</span></div>
    </div>
    <svg class="plant" style="left:0;top:320px" width="130" height="480" role="img" aria-label="Gezeichneter Leindotterblütenzweig vor blauem Aquarellfleck">
      <defs><radialGradient id="blueWash2"><stop offset="0" stop-color="#3f4fe0"/><stop offset="1" stop-color="#5a66d8" stop-opacity=".85"/></radialGradient></defs>
      <circle cx="82" cy="119" r="72" fill="url(#blueWash2)"/>
      <line x1="82" y1="45" x2="82" y2="476" stroke="var(--chalk-soft)" stroke-width="3" opacity=".7"/>
    </svg>
    <h2 class="title" style="left:124px;bottom:48px">LEIN<span class="title__accent">DOTTER</span>ÖL</h2>
    <div class="badge" style="left:174px;top:261px" role="img" aria-label="Omega-3 Siegel"></div>
    <ul class="benefits" style="left:187px;top:413px">
      <li>dynamisch</li><li>vital</li><li>kraftvoll</li><li>frisch<br>gepresst</li><li>naturbelassen</li><li>reich an<br>Omega3<br>Fettsäuren</li>
    </ul>
    <div class="volume" style="left:187px;top:760px">200ml</div>
  </section>

  <section class="label label--raps">
    <div class="brand">
      <div class="brand__row"><span class="brand__dot"></span><span class="brand__name">Wendrik</span></div>
    </div>
    <svg class="plant" style="left:0;top:310px" width="130" height="490" role="img" aria-label="Gezeichneter Rapsblütenzweig vor gelbem Aquarellfleck">
      <defs><radialGradient id="yellowWash"><stop offset="0" stop-color="#ecd566"/><stop offset="1" stop-color="#e3c23c" stop-opacity=".9"/></radialGradient></defs>
      <circle cx="76" cy="127" r="72" fill="url(#yellowWash)"/>
      <line x1="100" y1="60" x2="100" y2="484" stroke="var(--chalk)" stroke-width="2"/>
    </svg>
    <h2 class="title" style="left:122px;bottom:346px">RAPSÖL</h2>
    <div class="badge" style="left:168px;top:270px" role="img" aria-label="Omega-3 Siegel"></div>
    <ul class="benefits" style="left:129px;top:518px">
      <li>dynamisch</li><li>vital</li><li>kraftvoll</li><li>frisch<br>gepresst</li><li>naturbelassen</li><li>reich an<br>Omega3<br>Fettsäuren</li>
    </ul>
    <div class="volume" style="left:129px;top:763px">200ml</div>
  </section>

</main>
</body>
</html>
```